Blister Packaging Design for a Mouthguard

I need a clean and professional design for a mouthguard packaging.
the design should be clean, mostly black, white and grey. it should show our logo "VORTANEL". The Frontside schould show the German word "MUNDSCHUTZ" and smaller the Term "Mouthguard". the pfont should also show some parts in german flag colors to show we are a german company. at some place there has to be a place where the different style can be inserted. 4 main styles will be: "STRGL", "SPINDLE", "GLIMMER", "NEBEL TOR"
on the backside there need to be a place for the barcode and our company adress, detailes product description an maybe a picture of a drawed mouthguard.
Attached as well a finished design from some other company, just to show where the mouthguard will be placed in the packaging.
Target Market(s)
Boxing and Fighting sports in general
Industry/Entity Type
sport, fighting sports
Colors
Designer to choose only greyscale colors for use in the design.
Requirements
Must have
- clean and professional design
Nice to have
- German flag/Colors somewhere embedded on the front of the packaging
Should not have
- not too colorful

```html
<!DOCTYPE html>
<html lang="en">
<head>
<meta charset="utf-8">
<title>VORTANEL Mundschutz Blister Cards</title>
<link rel="stylesheet" href="https://fonts.googleapis.com/css2?family=Montserrat:wght@400;500;700;800&family=Orbitron:wght@700&family=Arimo:wght@400;700&display=swap">
<style>
  :root {
    --stage: #d1d2d4;
    --card-black: #050505;
    --strip-light: #f4f4f5;
    --strip-shade: #e2e3e5;
    --white: #ffffff;
    --pill: #e6e6e6;
    --pill-text: #3a3a3a;
    --hole: #d1d2d4;
    --faint-mark: #3a3a3a;
    --origin-blue: #1b9cc8;
    --flag-black: #111111;
    --flag-red: #dd0000;
    --flag-gold: #ffce00;
    --style-green: #7fc241;
    --style-red: #c8202a;
    --style-blue: #1d9cc8;
    --style-gold: #d9a92a;
    --back-card: #f2f2f4;
    --back-text: #1a1a1a;
    --back-line: #9a9a9c;
    --sketch-fill: #e6e7ea;
  }
  * { box-sizing: border-box; margin: 0; padding: 0; }
  html, body { width: 671px; height: 1200px; overflow: hidden; }
  body { background: var(--stage); position: relative; font-family: "Montserrat", sans-serif; }

  .card {
    position: absolute; width: 222px; height: 338px;
    border-radius: 12px; overflow: hidden;
    background: var(--card-black);
    box-shadow: 2px 3px 6px rgba(0,0,0,0.18);
  }
  .card--strgl   { left: 95px;  top: 55px;  --accent: var(--style-green); }
  .card--spindle { left: 346px; top: 55px;  --accent: var(--style-red); }
  .card--glimmer { left: 95px;  top: 407px; --accent: var(--style-blue); }
  .card--nebel   { left: 346px; top: 399px; --accent: var(--style-gold); }

  .hang-hole { position: absolute; left: 76px; top: 17px; width: 71px; height: 14px; background: var(--hole); border-radius: 7px; }
  .hang-hole::before { content: ""; position: absolute; left: 26px; top: -7px; width: 19px; height: 19px; border-radius: 50%; background: var(--hole); }

  .brand { position: absolute; left: 16px; top: 16px; width: 48px; display: flex; flex-direction: column; align-items: center; gap: 4px; }
  .brand__dot { width: 16px; height: 16px; border-radius: 50%; background: var(--white); }
  .brand__name { font-weight: 800; font-size: 7.5px; color: var(--white); letter-spacing: 0.2px; line-height: 1; }

  .size-pill { position: absolute; left: 165px; top: 15px; width: 43px; height: 10px; border-radius: 5px; background: var(--pill); color: var(--pill-text); font-size: 5.6px; font-weight: 700; text-align: center; line-height: 10px; }

  .title { position: absolute; left: 0; right: 0; top: 71px; text-align: center; color: var(--white); font-weight: 800; font-size: 24px; letter-spacing: 0.4px; line-height: 1; }
  .subtitle { position: absolute; left: 0; right: 0; top: 96px; text-align: center; color: var(--accent); font-weight: 500; font-size: 11.5px; line-height: 1; }

  .center-mark { position: absolute; left: 0; right: 0; top: 193px; display: flex; justify-content: center; align-items: center; gap: 7px; }
  .center-mark__dot { width: 22px; height: 22px; border-radius: 50%; background: var(--faint-mark); }
  .center-mark__name { color: var(--faint-mark); font-weight: 800; font-size: 24px; }

  .strip { position: absolute; left: 0; bottom: 0; width: 100%; height: 33px; background: linear-gradient(180deg, var(--strip-shade), var(--strip-light) 40%, var(--strip-light)); }
  .flag-dot { position: absolute; left: 13px; top: 6px; width: 16px; height: 16px; border-radius: 50%; overflow: hidden;
    background: linear-gradient(180deg, var(--flag-black) 0 33.3%, var(--flag-red) 33.3% 66.6%, var(--flag-gold) 66.6%); }
  .origin { position: absolute; left: 34px; top: 8px; color: var(--origin-blue); font-size: 5.6px; font-weight: 500; line-height: 6px; }
  .style-tab { position: absolute; right: 0; top: 9px; width: 90px; height: 24px; }
  .style-tab__name { position: absolute; right: 0; top: 9px; width: 84px; height: 24px; text-align: center; line-height: 24px; color: var(--white); font-family: "Orbitron", sans-serif; font-weight: 700; font-size: 9.5px; letter-spacing: 0.3px; }

  .back { position: absolute; left: 225px; top: 781px; width: 221px; height: 337px; border-radius: 12px; overflow: hidden; background: var(--back-card); box-shadow: 2px 3px 6px rgba(0,0,0,0.18); color: var(--back-text); font-family: "Arimo", sans-serif; }
  .back h3 { font-size: 5.8px; font-weight: 700; line-height: 7px; }
  .back .features { position: absolute; left: 15px; top: 70px; width: 95px; }
  .back ul { list-style: none; font-size: 5.2px; line-height: 6.5px; }
  .back ul li::before { content: "•"; margin-right: 3px; }
  .back .steps { position: absolute; left: 116px; top: 70px; width: 92px; }
  .back ol { font-size: 5.6px; line-height: 7.3px; padding-left: 10px; }
  .mouthguard-sketch { position: absolute; left: 13px; top: 118px; width: 93px; height: 77px; background: var(--sketch-fill); border-radius: 6px; }
  .warning { position: absolute; left: 15px; top: 212px; width: 192px; }
  .warning p { font-size: 5.2px; line-height: 6.5px; text-align: justify; }
  .back-mark { position: absolute; left: 24px; top: 293px; display: flex; align-items: center; gap: 3px; }
  .back-mark__dot { width: 8px; height: 8px; border-radius: 50%; background: #b9babd; }
  .back-mark__name { font-family: "Montserrat", sans-serif; font-weight: 800; font-size: 7.5px; color: #b9babd; }
  .barcode-slot { position: absolute; left: 118px; top: 277px; width: 87px; height: 45px; border: 0.6px solid var(--back-line); }
</style>
</head>
<body>

<article class="card card--strgl">
  <div class="brand"><span class="brand__dot"></span><span class="brand__name">VORTANEL</span></div>
  <div class="hang-hole"></div>
  <div class="size-pill">ADULT SIZE</div>
  <h1 class="title">MUNDSCHUTZ</h1>
  <p class="subtitle">MOUTHGUARD</p>
  <div class="center-mark"><span class="center-mark__dot"></span><span class="center-mark__name">VORTANEL</span></div>
  <footer class="strip">
    <span class="flag-dot"></span>
    <p class="origin">PRODUCT OF<br>GERMANY</p>
    <svg class="style-tab" viewBox="0 0 90 24"><polygon points="6,0 90,0 90,24 0,24" fill="var(--accent)"/></svg>
    <span class="style-tab__name">STRGL</span>
  </footer>
</article>

<article class="card card--spindle">
  <div class="brand"><span class="brand__dot"></span><span class="brand__name">VORTANEL</span></div>
  <div class="hang-hole"></div>
  <div class="size-pill">ADULT SIZE</div>
  <h1 class="title">MUNDSCHUTZ</h1>
  <p class="subtitle">MOUTHGUARD</p>
  <div class="center-mark"><span class="center-mark__dot"></span><span class="center-mark__name">VORTANEL</span></div>
  <footer class="strip">
    <span class="flag-dot"></span>
    <p class="origin">PRODUCT OF<br>GERMANY</p>
    <svg class="style-tab" viewBox="0 0 90 24"><polygon points="6,0 90,0 90,24 0,24" fill="var(--accent)"/></svg>
    <span class="style-tab__name">SPINDLE</span>
  </footer>
</article>

<article class="card card--glimmer">
  <div class="brand"><span class="brand__dot"></span><span class="brand__name">VORTANEL</span></div>
  <div class="hang-hole"></div>
  <div class="size-pill">ADULT SIZE</div>
  <h1 class="title">MUNDSCHUTZ</h1>
  <p class="subtitle">MOUTHGUARD</p>
  <div class="center-mark"><span class="center-mark__dot"></span><span class="center-mark__name">VORTANEL</span></div>
  <footer class="strip">
    <span class="flag-dot"></span>
    <p class="origin">PRODUCT OF<br>GERMANY</p>
    <svg class="style-tab" viewBox="0 0 90 24"><polygon points="6,0 90,0 90,24 0,24" fill="var(--accent)"/></svg>
    <span class="style-tab__name">GLIMMER</span>
  </footer>
</article>

<article class="card card--nebel">
  <div class="brand"><span class="brand__dot"></span><span class="brand__name">VORTANEL</span></div>
  <div class="hang-hole"></div>
  <div class="size-pill">ADULT SIZE</div>
  <h1 class="title">MUNDSCHUTZ</h1>
  <p class="subtitle">MOUTHGUARD</p>
  <div class="center-mark"><span class="center-mark__dot"></span><span class="center-mark__name">VORTANEL</span></div>
  <footer class="strip">
    <span class="flag-dot"></span>
    <p class="origin">PRODUCT OF<br>GERMANY</p>
    <svg class="style-tab" viewBox="0 0 90 24"><polygon points="6,0 90,0 90,24 0,24" fill="var(--accent)"/></svg>
    <span class="style-tab__name">NEBEL TOR</span>
  </footer>
</article>

<article class="back">
  <div class="hang-hole"></div>
  <section class="features">
    <h3>VORTANEL Mouth Guard</h3>
    <ul>
      <li>Material: EVA Material.</li>
      <li>Protective case included.</li>
      <li>Protects against impact.</li>
      <li>All types of contact sports.</li>
      <li>Do not use with braces.</li>
    </ul>
  </section>
  <div class="mouthguard-sketch" role="img" aria-label="Line drawing of the mouthguard with labels for shock absorber gel and anti-shock body"></div>
  <section class="steps">
    <h3>Molding steps:</h3>
    <ol>
      <li>Start by boiling water.</li>
      <li>Pour 200 ml into a bowl and leave for 30 seconds.</li>
      <li>Place the mouth guard in the water for 90 to 120 seconds.</li>
      <li>Align the mouth guard with the center of your mouth</li>
      <li>and press it upwards firmly, then bite down gently while aspiring. Use your fingers to push the edge of the mouth guard towards the gum line.</li>
      <li>Place the mouth guard in a bowl of cold water for 30 seconds.</li>
    </ol>
  </section>
  <section class="warning">
    <h3>WARNING:</h3>
    <p>Sports training can lead to injuries. Protective equipment will not eliminate all injuries, but may reduce the damage in some cases. Never practice without consulting your doctor. Always check your equipment before use. If you notice any defects, do not use the product.</p>
  </section>
  <div class="back-mark"><span class="back-mark__dot"></span><span class="back-mark__name">VORTANEL</span></div>
  <div class="barcode-slot"></div>
</article>

</body>
</html>
```